Phuket Thailand - Rental Villa Website

I have a villa for rent in Thailand and require a website - i need to demo pictures/walk through video, local attractions, villa facilities description plus seaonal rates and online booking.

Industry/Entity Type

Rental

Coding

Coded - Design and coding required

```html
<!DOCTYPE html>
<html lang="en">
<head>
<meta charset="utf-8">
<title>Palm Cove Villas – Phuket Villa Rental</title>
<link rel="stylesheet" href="https://fonts.googleapis.com/css2?family=Source+Sans+3:wght@300;400;600&family=Montserrat:wght@400;500&display=swap">
<style>
:root{
  --orange:#f15a22;
  --green:#3a9a3a;
  --ink:#222;
  --panel:rgba(12,22,45,.72);
  --white:#fff;
  --footer:#000;
  --bar:#222;
  --field-text:#777;
}
*{margin:0;padding:0;box-sizing:border-box}
html,body{width:786px;height:1200px;overflow:hidden;background:#fff}
body{position:relative;font-family:"Source Sans 3",sans-serif;font-weight:400;color:var(--ink)}
.abs{position:absolute}
.hero{left:0;top:0;width:786px;height:402px;background:
  radial-gradient(ellipse 260px 90px at 420px 180px,rgba(255,190,90,.45),transparent 70%),
  linear-gradient(180deg,#0c1836 0%,#1b2c55 35%,#3a2a2a 65%,#6a3f25 85%,#2a1a14 100%)}
.logo{left:61px;top:28px;font-size:17px;font-weight:600;color:var(--white);letter-spacing:.5px}
.nav a{position:absolute;top:30px;font-size:10.5px;color:#dfe4ee;text-decoration:none;font-weight:300}
.nav .home{left:422px;top:0;width:45px;height:54px;background:#0a1428;padding-top:30px;text-align:center;color:#fff}
.search{left:62px;top:82px;width:194px;height:320px;background:var(--panel);color:#fff}
.search h2{position:absolute;left:0;width:194px;top:12px;text-align:center;font-weight:300;font-size:15px;letter-spacing:.3px}
.search .sub{position:absolute;left:0;width:194px;top:35px;text-align:center;font-size:10px;font-weight:400}
.field{position:absolute;background:#fff;height:20px;font-size:7.5px;font-weight:400;color:var(--field-text);padding:6px 8px}
.field::after{content:"";position:absolute;right:7px;top:9px;border:3px solid transparent;border-top:3px solid #555}
.lbl{position:absolute;font-size:9.5px;font-weight:300}
.small{font-size:7.5px;font-weight:400}
.radio{display:inline-block;width:7px;height:7px;border-radius:50%;border:1px solid #fff;vertical-align:-1px;margin:0 3px 0 6px}
.radio.on{background:#ddd}
.book{left:11px;top:270px;width:171px;height:22px;background:var(--orange);color:#fff;font-size:14px;text-align:center;line-height:22px;font-weight:300}
.welcome{left:445px;top:204px;font-family:Montserrat,sans-serif;font-size:24px;color:#fff;font-weight:500}
.welcome-copy{left:447px;top:239px;width:210px;font-size:9px;font-weight:400;color:#e8e8e8;line-height:12px}
.arrows{font-size:16px;color:#fff}
.tile{top:402px;height:180px}
.tile span{position:absolute;color:#fff;font-size:15px;font-weight:300}
h3.sec{position:absolute;font-weight:400;font-size:15.5px;color:#222}
.copy{left:51px;top:623px;width:304px;font-size:7.6px;font-weight:400;line-height:14.4px;text-align:justify;color:#111}
.card{top:762px;width:226px}
.card .photo{height:126px}
.card h4{position:absolute;left:5px;top:131px;font-weight:400;font-size:14.5px}
.card .rev{position:absolute;right:7px;top:136px;font-size:8px;font-weight:400}
.card .stars{position:absolute;right:7px;top:150px;font-size:7px;color:var(--orange);letter-spacing:5px}
.card .meta{position:absolute;left:5px;top:159px;font-size:8px;font-weight:400;line-height:14.5px}
.card .price{position:absolute;left:4px;top:187px;font-size:12.5px;color:var(--green);font-weight:300}
.card .btn{position:absolute;left:139px;top:182px;width:85px;height:22px;background:var(--orange);color:#fff;font-size:8.5px;font-weight:400;text-align:center;line-height:22px}
.footer{left:0;top:990px;width:786px;height:186px;background:var(--footer);color:#fff}
.footer h5{position:absolute;top:24px;font-family:Montserrat,sans-serif;font-weight:500;font-size:13.5px;letter-spacing:.3px}
.footer ul{position:absolute;top:50px;list-style:none;font-size:8.3px;font-weight:400;line-height:14.5px}
.footer p{position:absolute;font-size:8.3px;font-weight:400;line-height:14.5px}
.email{left:440px;top:83px;width:119px;height:21px;background:#fff;color:#777;font-size:7.5px;font-weight:400;padding:6px 8px}
.subscribe{left:440px;top:112px;width:119px;height:21px;background:#2a2a2a;font-size:9.5px;text-align:center;line-height:21px;font-weight:600}
.social{position:absolute;top:55px;width:18px;height:18px;border-radius:50%}
.bottom{left:0;top:1176px;width:786px;height:24px;background:var(--bar);color:#ddd;font-size:7.5px;font-weight:400;text-align:right;padding:6px 49px 0 0}
</style>
</head>
<body>
<header class="abs hero" role="img" aria-label="Night view of a lit wooden pier and palm trees at the villa resort"></header>
<div class="abs logo">PALM COVE VILLAS</div>
<nav class="nav">
  <a class="home" href="#">Home</a>
  <a href="#" style="left:478px">About Us</a>
  <a href="#" style="left:537px">Services</a>
  <a href="#" style="left:591px">Online Booking</a>
  <a href="#" style="left:677px">Contact Us</a>
</nav>

<section class="abs search">
  <h2>SEARCH VILLAS</h2>
  <div class="sub">Online Booking</div>
  <div class="field" style="left:12px;top:62px;width:170px">Destination</div>
  <div class="lbl small" style="left:14px;top:95px">Travelling for:<span class="radio"></span>Business<span class="radio on"></span>Leisure</div>
  <div class="lbl" style="left:14px;top:114px">Check-in date</div>
  <svg class="abs" style="left:21px;top:141px" width="9" height="9" viewBox="0 0 9 9"><rect x=".5" y="1.5" width="8" height="7" fill="none" stroke="#ccc"/><rect x=".5" y="1.5" width="8" height="2" fill="#ccc"/></svg>
  <div class="field" style="left:36px;top:136px;width:60px">Day</div>
  <div class="field" style="left:103px;top:136px;width:79px">Month</div>
  <div class="lbl" style="left:14px;top:166px">Check-out date</div>
  <svg class="abs" style="left:21px;top:193px" width="9" height="9" viewBox="0 0 9 9"><rect x=".5" y="1.5" width="8" height="7" fill="none" stroke="#ccc"/><rect x=".5" y="1.5" width="8" height="2" fill="#ccc"/></svg>
  <div class="field" style="left:36px;top:188px;width:60px">Day</div>
  <div class="field" style="left:103px;top:188px;width:79px">Month</div>
  <div class="lbl small" style="left:22px;top:220px"><span style="display:inline-block;width:6px;height:6px;background:#ddd;margin-right:5px"></span>I don't have specific dates yet</div>
  <div class="lbl" style="left:14px;top:245px">Guests</div>
  <div class="field" style="left:51px;top:240px;width:131px">2 Adults , 0 Children</div>
  <div class="abs book">Book Now</div>
</section>

<h1 class="abs welcome">WELCOME TEXT</h1>
<p class="abs welcome-copy">Lorem ipsum dolor sit amet, consec tetuer adipi scing elit. Praesent vestibulum molestie lacuiirhs.</p>
<div class="abs arrows" style="left:688px;top:364px">&#8249;&nbsp;&nbsp;&#8250;</div>

<div class="abs tile" style="left:39px;width:250px;background:linear-gradient(135deg,#6b625a,#a9a39b 50%,#3b3836)" role="img" aria-label="Villa bedroom interior with video play button"><svg class="abs" style="left:102px;top:70px" width="42" height="42" viewBox="0 0 42 42"><circle cx="21" cy="21" r="21" fill="rgba(0,0,0,.55)"/><path d="M16 12 L30 21 L16 30Z" fill="#fff"/></svg><span style="left:58px;top:114px">Walk through video</span></div>
<div class="abs tile" style="left:290px;width:204px;background:linear-gradient(160deg,#4a2e1e,#8a6a52 45%,#9fb0a8 75%,#6e6e68)" role="img" aria-label="Timber pavilion roof overlooking local scenery"><span style="left:87px;top:20px">Local attractions</span></div>
<div class="abs tile" style="left:495px;width:252px;background:linear-gradient(170deg,#c9d0d6,#6c7a66 40%,#8b7b66 65%,#c7c2b8)" role="img" aria-label="Pavilion terrace facing a lake and hills"><span style="left:137px;top:117px">Seasonal rates</span><span style="left:163px;top:145px">50% Offer</span></div>

<h3 class="sec" style="left:51px;top:594px">Villa Facilities</h3>
<div class="abs copy"><p>Lorem ipsum dolor sit amet, consectetur adipiscing elit, sed do eiusmod tempor incididunt ut labore et dolore magna aliqua. Ut enim ad minim veniam, quis nostrud exercitation ullamco laboris nisi ut aliquip ex ea commodo consequat.</p><p style="margin-top:14px">Duis aute irure dolor in reprehenderit in voluptate velit esse cillum dolore eu fugiat nulla pariatur</p></div>
<div class="abs" style="left:375px;top:598px;width:372px;height:115px;background:linear-gradient(100deg,#5a6a3c,#c8c8cc 25%,#4a4d55 50%,#8a6e66 75%,#6e5650)" role="img" aria-label="Villa exterior with tiled roof and garden"></div>

<h3 class="sec" style="left:51px;top:733px">Featured Villas</h3>
<div class="abs" style="left:709px;top:724px;font-size:20px;color:#222">&#8249;&nbsp;&#8250;</div>

<article class="abs card" style="left:39px">
  <div class="photo" style="background:linear-gradient(180deg,#2a3a66,#c7bfae 45%,#2c3c5a)" role="img" aria-label="Villa courtyard with pool at dusk"></div>
  <h4>Lorium Ipsum</h4><div class="rev">2 Reviews</div><div class="stars">★★★★★</div>
  <div class="meta">Surin, Phuket, Thailand<br>5 Bedrooms, 5 Bathrooms, Pool</div>
  <div class="price">$750 - $2,900 /night</div><div class="btn">View Villa Details</div>
</article>
<article class="abs card" style="left:280px">
  <div class="photo" style="background:linear-gradient(170deg,#6a7068,#8fb3ae 40%,#5f8f8c 80%,#4a6a68)" role="img" aria-label="Infinity pool with clear water"></div>
  <h4>Lorium Ipsum</h4><div class="rev">2 Reviews</div><div class="stars">★★★★★</div>
  <div class="meta">Surin, Phuket, Thailand<br>5 Bedrooms, 5 Bathrooms, Pool</div>
  <div class="price">$750 - $2,900 /night</div><div class="btn">View Villa Details</div>
</article>
<article class="abs card" style="left:521px">
  <div class="photo" style="background:linear-gradient(180deg,#3d5a2e,#6f8a4c 40%,#b07a55 70%,#7a4a30)" role="img" aria-label="Poolside deck with loungers and umbrellas among palms"></div>
  <h4>Lorium Ipsum</h4><div class="rev">2 Reviews</div><div class="stars">★★★★★</div>
  <div class="meta">Surin, Phuket, Thailand<br>5 Bedrooms, 5 Bathrooms, Pool</div>
  <div class="price">$750 - $2,900 /night</div><div class="btn">View Villa Details</div>
</article>

<footer class="abs footer">
  <h5 style="left:74px">QUICK LINKS</h5>
  <ul style="left:77px"><li>Home</li><li>About Us</li><li>Services</li><li>Online Booking</li><li>Contact Us</li></ul>
  <h5 style="left:250px">CONTACT INFO</h5>
  <svg class="abs" style="left:252px;top:53px" width="9" height="8" viewBox="0 0 9 8"><path d="M4.5 0L9 4H7.5V8H1.5V4H0Z" fill="#fff"/></svg>
  <p style="left:268px;top:50px">Company name<br>Unit 406, 4th Floor,<br>Lorem Ipsum is simply,<br>Sector-x, Lakeview - 450210</p>
  <svg class="abs" style="left:255px;top:124px" width="6" height="10" viewBox="0 0 6 10"><rect x=".5" y=".5" width="5" height="9" rx="1" fill="none" stroke="#fff"/></svg>
  <p style="left:268px;top:121px">Phone : 000-000-0000</p>
  <svg class="abs" style="left:254px;top:153px" width="9" height="8" viewBox="0 0 9 8"><rect x="0" y="3" width="9" height="5" fill="#fff"/><rect x="2" y="0" width="5" height="3" fill="#fff"/></svg>
  <p style="left:268px;top:150px">Fax : 000 - 000 - 0000</p>
  <h5 style="left:438px">NEWSLETTER</h5>
  <p style="left:440px;top:50px;width:120px">Sign up to receive the latest updates</p>
  <div class="abs email">&#9993; Email id</div>
  <div class="abs subscribe">SUBSCRIBE</div>
  <h5 style="left:614px">FOLLOW US</h5>
  <span class="social" style="left:609px;background:#3b5998"></span>
  <span class="social" style="left:633px;background:#1da1f2"></span>
  <span class="social" style="left:657px;background:#0e76a8"></span>
  <span class="social" style="left:682px;background:#d34836"></span>
</footer>
<div class="abs bottom">© 2015.www.companyname.com. All rights reserved.</div>
</body>
</html>
```